Electrician Letterhead Design BLR

We need some letterhead for our bills and other papers.
Customer address is on the right side (Swiss format)
A4 format

Design should also be applicable on Cards

Target Market(s)

Private Customers, Small Business

Industry/Entity Type

Electrician

Other font styles liked:
• incised 901

Colors
00AB8E
00BBA5
67D7C9
C6EFE9
E9F9F6

```html
<!DOCTYPE html>
<html lang="en">
<head>
<meta charset="utf-8">
<title>BLR Letterhead</title>
<link rel="stylesheet" href="https://fonts.googleapis.com/css2?family=Poppins:wght@400;500;600;700&family=Pinyon+Script&display=swap">
<style>
  :root {
    --backdrop: #9b9b9b;
    --paper: #ffffff;
    --teal: #2aa898;
    --teal-soft: #80bdb4;
    --charcoal: #363636;
    --rule-grey: #c4c4c4;
    --ink: #333333;
    --ink-soft: #6b6b6b;
  }
  * { margin: 0; padding: 0; box-sizing: border-box; }
  html, body {
    width: 870px; height: 1200px; overflow: hidden;
    background: var(--backdrop);
    font-family: "Poppins", sans-serif;
  }
  .canvas { position: relative; width: 870px; height: 1200px; }
  .sheet {
    position: absolute; left: 64px; top: 71px;
    width: 743px; height: 1057px; background: var(--paper);
  }
  .sheet-shapes { position: absolute; left: 0; top: 0; width: 870px; height: 1200px; }
  .text { position: absolute; }

  .brand-square { position: absolute; left: 64px; top: 137.5px; width: 46px; height: 43px; background: var(--teal); }
  .brand-name {
    left: 140px; top: 124px; font-size: 58px; font-weight: 700;
    color: var(--teal); line-height: 1; letter-spacing: 1px;
  }
  .brand-tagline {
    left: 142px; top: 184px; font-size: 8px; font-weight: 500;
    color: var(--ink); letter-spacing: 0.3px;
  }
  .header-rule { position: absolute; left: 324px; top: 174px; width: 357px; height: 7px; background: var(--rule-grey); }

  .sender { left: 142px; top: 278px; color: var(--ink); }
  .sender-name { font-size: 18px; font-weight: 600; line-height: 1.1; }
  .sender-role { font-size: 11.5px; line-height: 1.2; }

  .contact { left: 142px; top: 322px; font-size: 11px; line-height: 17px; color: var(--ink-soft); }
  .contact li { list-style: none; }
  .contact li:first-child { color: var(--ink); }
  .contact .label { display: inline-block; width: 20px; }

  .letter-date { left: 544px; top: 341px; font-size: 11px; color: var(--ink-soft); }

  .letter-body {
    left: 142px; top: 400px; width: 541px;
    font-size: 10.6px; line-height: 17px; color: var(--ink-soft);
    text-align: justify;
  }
  .letter-body p + p { margin-top: 16.5px; }

  .signature {
    left: 140px; top: 752px; font-family: "Pinyon Script", cursive;
    font-size: 24px; color: var(--ink);
  }
  .signer { left: 142px; top: 792px; color: var(--ink); }
  .signer-name { font-size: 13.7px; font-weight: 600; line-height: 1.2; }
  .signer-role { font-size: 9.5px; line-height: 1.4; }

  .footer-item { position: absolute; top: 909px; display: flex; align-items: center; gap: 9px; }
  .footer-item svg { width: 30px; height: 30px; flex: none; }
  .footer-lines { font-size: 12.5px; line-height: 17.5px; color: var(--ink-soft); letter-spacing: 0.4px; }
  .footer-phone { left: 141px; }
  .footer-web { left: 312px; }
  .footer-address { left: 508px; }
</style>
</head>
<body>
<div class="canvas">
  <div class="sheet"></div>

  <svg class="sheet-shapes" viewBox="0 0 870 1200" aria-hidden="true">
    <path d="M759 71 H807 V1128 H660 L536 1015.5 H656 A103 103 0 0 0 759 912.5 Z" fill="var(--teal-soft)"/>
    <polygon points="507,1016.5 632,1128 382,1128" fill="var(--teal)"/>
    <polygon points="64,1082 405,1082 354,1128 64,1128" fill="var(--charcoal)"/>
    <polygon points="64,1062.5 425,1062.5 418,1069 64,1069" fill="var(--teal)"/>
  </svg>

  <div class="brand-square"></div>
  <div class="text brand-name">BLR</div>
  <div class="text brand-tagline">Blauried Elektrotechnik AG</div>
  <div class="header-rule"></div>

  <div class="text sender">
    <div class="sender-name">Lorem ipsum</div>
    <div class="sender-role">Creative Director</div>
  </div>

  <ul class="text contact">
    <li><span class="label">A :</span>Lorem ipsum dolor sit amet, consectetuer</li>
    <li><span class="label">W :</span>Lorem ipsum dolor sit amet, consectetuer</li>
    <li><span class="label">P :</span>+00- 00000 - 0000</li>
  </ul>

  <div class="text letter-date">Date: 10 September, 2020</div>

  <div class="text letter-body">
    <p>Lorem ipsum dolor sit amet, consectetuer adipiscing elit, sed diam nonummy nibh euismod tincidunt ut laoreet dolore magna aliquam erat volutpat. Ut wisi enim ad minim veniam, quis nostrud exerci tation ullamcorper suscipit lobortis nisl ut aliquip ex ea commodo consequat.Lorem ipsum dolor sit amet, consectetuer adipiscing elit, sed diam nonummy nibh euismod tincidunt ut laoreet dolore magna aliquam erat volutpat. Ut wisi enim ad minim veniam,</p>
    <p>Lorem ipsum dolor sit amet, consectetuer adipiscing elit, sed diam nonummy nibh euismod tincidunt ut laoreet dolore magna aliquam erat volutpat. Ut wisi enim ad minim veniam, quis nostrud exerci tation ullamcorper suscipit lobortis nisl ut aliquip ex ea commodo consequat.Lorem ipsum dolor</p>
    <p>Lorem ipsum dolor sit amet, consectetuer adipiscing elit, sed diam nonummy nibh euismod tincidunt ut laoreet dolore magna aliquam erat volutpat. Ut wisi enim ad minim veniam, quis nostrud exerci tation ullamcorper suscipit lobortis nisl ut aliquip ex ea commodo consequat.Lorem ipsum dolor sit amet, consectetuer adipiscing elit, sed diam nonummy nibh euismod tincidunt ut laoreet dolore magna aliquam erat volutpat. Ut wisi enim ad minim veniam,</p>
    <p>Lorem ipsum dolor sit amet, consectetuer adipiscing elit, sed diam nonummy nibh euismod tincidunt ut laoreet dolore magna aliquam erat volutpat. Ut wisi enim ad minim veniam, quis nostrud exerci tation ullamcorper suscipit lobortis nisl ut aliquip ex ea commodo consequat.Lorem ipsum dolor</p>
  </div>

  <div class="text signature">Lorem ipsum</div>
  <div class="text signer">
    <div class="signer-name">Lorem ipsum</div>
    <div class="signer-role">Manager</div>
  </div>

  <div class="footer-item footer-phone">
    <svg viewBox="0 0 30 30" aria-hidden="true">
      <circle cx="15" cy="15" r="13.5" fill="none" stroke="var(--teal)" stroke-width="1.4"/>
      <path d="M10.5 9 l2.2 -0.6 1.4 3 -1.4 1.1 c0.8 1.8 2 3 3.8 3.8 l1.1 -1.4 3 1.4 -0.6 2.2 c-5.2 0.4 -9.9 -4.3 -9.5 -9.5 z" fill="none" stroke="var(--teal)" stroke-width="1.2" stroke-linejoin="round"/>
      <path d="M16.5 9.5 a4 4 0 0 1 4 4 M16.5 7 a6.5 6.5 0 0 1 6.5 6.5" fill="none" stroke="var(--teal)" stroke-width="1.1" stroke-linecap="round"/>
    </svg>
    <div class="footer-lines">+000 0000 0000<br>+000 0000 0000</div>
  </div>

  <div class="footer-item footer-web">
    <svg viewBox="0 0 30 30" aria-hidden="true">
      <circle cx="15" cy="15" r="13.5" fill="none" stroke="var(--teal)" stroke-width="1.4"/>
      <circle cx="15" cy="15" r="7.5" fill="none" stroke="var(--teal)" stroke-width="1.2"/>
      <ellipse cx="15" cy="15" rx="3.2" ry="7.5" fill="none" stroke="var(--teal)" stroke-width="1.1"/>
      <path d="M7.5 15 H22.5 M9 11 H21 M9 19 H21" stroke="var(--teal)" stroke-width="1.1"/>
    </svg>
    <div class="footer-lines">YOURSITEGOESHERE<br>YOURSITEGOESHERE</div>
  </div>

  <div class="footer-item footer-address">
    <svg viewBox="0 0 30 30" aria-hidden="true">
      <circle cx="15" cy="15" r="13.5" fill="none" stroke="var(--teal)" stroke-width="1.4"/>
      <path d="M15 23 c-3.5 -4 -5.5 -7 -5.5 -9.5 a5.5 5.5 0 0 1 11 0 c0 2.5 -2 5.5 -5.5 9.5 z" fill="none" stroke="var(--teal)" stroke-width="1.2" stroke-linejoin="round"/>
      <circle cx="15" cy="13.5" r="2" fill="none" stroke="var(--teal)" stroke-width="1.1"/>
    </svg>
    <div class="footer-lines">STREET ADDRESS HERE<br>LOREM, 0000</div>
  </div>
</div>
</body>
</html>
```